New Web Design Project

New Roofing Website homepage mockup

Complete design document here: https://files.plorvex.net/doc/7tQmZrA2kLwP9xVbN4cYhE3sJdF8gUoR6iKe1nTy/edit?usp=sharing
Updates

Number of Pages Required

1 page

Font styles to use
Sans Serif

```html
<!DOCTYPE html>
<html lang="en">
<head>
<meta charset="utf-8">
<title>Ridgeline Roofing — Home</title>
<link rel="stylesheet" href="https://fonts.googleapis.com/css2?family=Open+Sans:wght@300;400;600;700;800&display=swap">
<style>
:root{
  --blue:#0a84cc;
  --blue-dark:#0669a8;
  --blue-light:#7cc4ea;
  --ink:#3c3c3c;
  --muted:#8a8a8a;
  --rule:#cfcfcf;
  --card:#dcdcdc;
  --black:#050505;
  --white:#ffffff;
}
*{box-sizing:border-box;margin:0;padding:0}
html,body{width:1200px;height:3659px;overflow:hidden}
body{font-family:"Open Sans",Arial,sans-serif;color:var(--ink);background:var(--white);position:relative}
.abs{position:absolute}
.wrap{position:absolute;left:234px;width:732px}

/* top bar */
.topbar{position:absolute;top:0;left:0;width:1200px;height:26px;background:var(--blue);color:var(--white);font-size:10px}
.topbar .item{position:absolute;top:6px;display:flex;align-items:center;gap:8px}
.topbar .social{position:absolute;right:240px;top:6px;display:flex;gap:14px}
.topbar .social span{width:11px;height:11px;border:1.4px solid rgba(255,255,255,.85);border-radius:50%}

/* nav */
.nav{position:absolute;top:26px;left:0;width:1200px;height:64px;background:var(--white);border-bottom:1px solid #eee}
.brand{position:absolute;left:234px;top:20px;display:flex;align-items:center;gap:7px;font-weight:700;font-size:14px;color:var(--blue);letter-spacing:.3px}
.brand i{display:block;width:12px;height:12px;background:var(--blue)}
.menu{position:absolute;right:234px;top:28px;display:flex;gap:18px;font-size:9px;color:#555;letter-spacing:.2px}
.menu .active{color:var(--blue)}

/* hero */
.hero{position:absolute;top:90px;left:0;width:1200px;height:500px;background:linear-gradient(180deg,#8aa3bf 0%,#6d7a8a 35%,#9aa0a6 70%,#5e5e5c 100%)}
.hero svg{position:absolute;left:0;top:0}
.hero h1{position:absolute;left:64px;top:290px;font-size:44px;line-height:54px;font-weight:700;color:var(--white);letter-spacing:-.5px}
.btn-white{position:absolute;left:67px;top:418px;width:190px;height:30px;background:var(--white);color:var(--blue-dark);border-radius:4px;font-size:10px;font-weight:700;display:flex;align-items:center;justify-content:center}

.section-title{position:absolute;left:0;width:1200px;text-align:center;font-size:30px;font-weight:700;color:#444}

/* services */
.service{position:absolute;width:220px;text-align:center}
.ring{width:112px;height:112px;margin:0 auto;border-radius:50%;background:var(--blue-light);display:flex;align-items:center;justify-content:center}
.ring .mid{width:98px;height:98px;border-radius:50%;background:var(--blue);display:flex;align-items:center;justify-content:center}
.ring .core{width:78px;height:78px;border-radius:50%;background:var(--white);display:flex;align-items:center;justify-content:center}
.service h3{margin-top:12px;font-size:13px;font-weight:700;color:#333}
.service p{margin-top:4px;font-size:10px;line-height:16px;color:var(--muted)}

/* about */
.about h2{font-size:30px;font-weight:700;color:#444}
.about p{margin-top:12px;width:310px;font-size:11px;line-height:21px;color:var(--muted)}
.btn-blue{display:flex;align-items:center;justify-content:center;background:var(--blue);color:var(--white);font-size:10px;font-weight:700;border-radius:4px}
.about .btn-blue{margin-top:14px;width:108px;height:29px}
.photo-shadow{position:absolute;left:601px;top:1315px;width:352px;height:190px;background:#e6e6e6}
.team-photo{position:absolute;left:584px;top:1299px;width:353px;height:188px;background:linear-gradient(180deg,#bcd2e4 0%,#6f7f8b 45%,#262a2e 70%,#9c9c94 100%)}

/* roof types */
.tabs{position:absolute;left:234px;top:1696px;width:730px;height:31px;background:var(--black);display:flex;font-size:10px;color:var(--white)}
.tabs span{display:flex;align-items:center;justify-content:center}
.tabs .on{background:var(--blue)}
.roof-img{position:absolute;top:1740px;width:232px;height:126px}

/* projects */
.projects{position:absolute;top:1954px;left:0;width:1200px;height:476px;background:linear-gradient(180deg,#0d7fc2 0%,#0a88d0 50%,#0b86cc 100%)}
.projects .section-title{color:var(--white);top:40px}
.tile{position:absolute}
.tile-label{position:absolute;inset:0;display:flex;align-items:center;justify-content:center;color:var(--white);font-size:18px;letter-spacing:.4px}

/* estimate */
.step{position:absolute;top:2585px;width:168px;border-bottom:1px solid var(--rule);padding-bottom:4px;font-size:10px;color:#555;display:flex;align-items:baseline;gap:9px}
.step b{font-size:15px;font-weight:400;color:#333}
.est{position:absolute;top:2637px;width:168px;height:308px;background:var(--card);text-align:center}
.est .shingle{height:140px}
.est .grade{margin-top:18px;font-size:10px;color:#777}
.est .model{margin-top:12px;font-size:10px;color:#777}
.est .price{margin-top:8px;font-size:13px;font-weight:700;color:#888}
.est .info{margin-top:8px;font-size:8px;color:#444}
.est .btn-blue{margin:12px auto 0;width:140px;height:29px;font-size:8.5px}

/* testimonials */
.quote{position:absolute;border-radius:8px;font-size:8.5px;line-height:14px;padding:34px 12px 12px 44px}
.quote .mark{position:absolute;left:12px;top:14px}
.quote.side{background:#f1f1f1;color:#c0c0c0;width:202px;height:154px;top:3117px}
.quote.main{background:var(--blue);color:var(--white);width:234px;height:180px;top:3104px;padding-top:32px}
.quote.main:after{content:"";position:absolute;left:50%;bottom:-8px;margin-left:-8px;border:8px solid transparent;border-bottom:0;border-top-color:var(--blue)}
.client{position:absolute;top:3306px;text-align:center;width:202px}
.client b{display:block;font-size:15px;font-weight:400}
.client span{font-size:10px;letter-spacing:1px}

/* footer */
.footer{position:absolute;top:3436px;left:0;width:1200px;height:223px;background:var(--black);color:#9a9a9a;font-size:8px}
.footer .fname{position:absolute;left:234px;top:82px;display:flex;align-items:center;gap:8px;font-size:18px;font-weight:700;color:var(--blue)}
.footer .fname i{display:block;width:14px;height:14px;background:var(--blue)}
.footer .addr{position:absolute;left:234px;width:170px;top:148px;text-align:center;line-height:16px}
.footer h4{position:absolute;top:46px;font-size:11px;font-weight:700;color:var(--blue)}
.links{position:absolute;left:548px;top:88px;display:grid;grid-template-columns:80px 80px;row-gap:10px}
.contact{position:absolute;left:797px;top:86px;display:flex;flex-direction:column;gap:13px}
.contact div{display:flex;align-items:center;gap:8px}
.fsocial{display:flex;gap:14px}
.fsocial span{width:10px;height:10px;border:1.3px solid #777;border-radius:50%}
</style>
</head>
<body>

<header class="topbar">
  <div class="item" style="left:234px">
    <svg width="12" height="12" viewBox="0 0 24 24" fill="none" stroke="#fff" stroke-width="2"><path d="M5 3h4l2 5-3 2a12 12 0 0 0 6 6l2-3 5 2v4a2 2 0 0 1-2 2A18 18 0 0 1 3 5a2 2 0 0 1 2-2z"/></svg>
    555-014-2290
  </div>
  <div class="item" style="left:360px">
    <svg width="13" height="10" viewBox="0 0 26 18" fill="none" stroke="#fff" stroke-width="2"><rect x="1" y="1" width="24" height="16"/><path d="M1 1l12 9 12-9"/></svg>
    hello@ridgelineroofing.example
  </div>
  <div class="social"><span></span><span></span><span></span><span></span></div>
</header>

<nav class="nav">
  <div class="brand"><i></i>RIDGELINE ROOFING</div>
  <div class="menu">
    <span class="active">HOME</span><span>RIDGELINE ROOFING</span><span>BLOG</span><span>REVIEWS</span><span>ABOUT</span><span>SERVICES</span><span>AFFILIATIONS</span><span>CONTACT</span>
  </div>
</nav>

<section class="hero" role="img" aria-label="Photo of a large grey-sided house with dormers and a three-car garage under a blue sky">
  <svg width="1200" height="500" aria-hidden="true"><polygon points="0,251 340,251 590,500 0,500" fill="#0a84cc" fill-opacity=".93"/></svg>
  <h1>BUILT RIGHT,<br>BUILT TO LAST</h1>
  <div class="btn-white">GET AN INSTANT ESTIMATE</div>
</section>

<h2 class="section-title" style="top:674px">SERVICES</h2>

<div class="service" style="left:218px;top:770px">
  <div class="ring"><div class="mid"><div class="core">
    <svg width="30" height="30" viewBox="0 0 30 30" fill="none" stroke="#333" stroke-width="1.5"><path d="M4 22h22M6 18h18l-2-4H8z"/><path d="M12 14V8h3v6M16 10l4-3"/><path d="M4 26h22"/></svg>
  </div></div></div>
  <h3>Roof Installation</h3>
  <p>Aorem ipsum dolor sit amet, consect<br>etur adipiscing elit, sed .</p>
</div>
<div class="service" style="left:479px;top:770px">
  <div class="ring"><div class="mid"><div class="core">
    <svg width="30" height="30" viewBox="0 0 30 30" fill="none" stroke="#333" stroke-width="1.5"><path d="M3 15L15 5l12 10M7 12v13h16V12"/><path d="M12 25v-7h6v7"/></svg>
  </div></div></div>
  <h3>Roof Repair</h3>
  <p>Aorem ipsum dolor sit amet, consect<br>etur adipiscing elit, sed .</p>
</div>
<div class="service" style="left:730px;top:770px">
  <div class="ring"><div class="mid"><div class="core">
    <svg width="30" height="30" viewBox="0 0 30 30" fill="none" stroke="#333" stroke-width="1.5"><path d="M3 15L15 5l12 10M7 12v13h16V12"/><rect x="11" y="14" width="8" height="7"/><path d="M15 14v7M11 17.5h8"/></svg>
  </div></div></div>
  <h3>Windows/Skylights</h3>
  <p>Aorem ipsum dolor sit amet, consect<br>etur adipiscing elit, sed .</p>
</div>
<div class="service" style="left:218px;top:1002px">
  <div class="ring"><div class="mid"><div class="core">
    <svg width="30" height="30" viewBox="0 0 30 30" fill="none" stroke="#333" stroke-width="1.5"><path d="M5 14L15 6l10 8M8 12v13h14V12"/><path d="M4 14h22"/><rect x="12" y="17" width="6" height="8"/></svg>
  </div></div></div>
  <h3>Gutters</h3>
  <p>Aorem ipsum dolor sit amet, consect<br>etur adipiscing elit, sed .</p>
</div>
<div class="service" style="left:479px;top:1002px">
  <div class="ring"><div class="mid"><div class="core">
    <svg width="30" height="30" viewBox="0 0 30 30" fill="none" stroke="#333" stroke-width="1.5"><rect x="7" y="5" width="16" height="20"/><path d="M7 11h16M15 11v14M10 8h10"/></svg>
  </div></div></div>
  <h3>Siding</h3>
  <p>Aorem ipsum dolor sit amet, consect<br>etur adipiscing elit, sed .</p>
</div>
<div class="service" style="left:730px;top:1002px">
  <div class="ring"><div class="mid"><div class="core">
    <svg width="30" height="30" viewBox="0 0 30 30" fill="none" stroke="#333" stroke-width="1.5"><path d="M8 6v6a7 7 0 0 0 14 0V6M12 6v6M15 6v7M18 6v6"/><path d="M15 19v3"/><path d="M15 24c-1 1.5-1 3 0 3s1-1.5 0-3z"/></svg>
  </div></div></div>
  <h3>Interior leak damage repairs</h3>
  <p>Aorem ipsum dolor sit amet, consect<br>etur adipiscing elit, sed .</p>
</div>

<section class="wrap about" style="top:1290px">
  <h2>ABOUT</h2>
  <p>After over a decade of general contracting we continue to see a repetitive trend by the roof purchase process where home owners are constantly left confused, nervous and worried when they need a new roof. As one of the most important features of keeping your home safe, this is un-acceptable. Ridgeline Roofing was created to break this trend.</p>
  <div class="btn-blue">READ MORE</div>
</section>
<div class="photo-shadow"></div>
<div class="team-photo" role="img" aria-label="Photo of the roofing team standing beside a black company pickup truck"></div>

<h2 class="section-title" style="top:1607px">TYPES OF ROOFS</h2>
<div class="tabs">
  <span class="on" style="width:143px">Cedar</span><span style="width:160px">Metal</span><span style="width:113px">Slate</span><span style="width:157px">Asphalt</span><span style="width:157px">Rubber</span>
</div>
<div class="roof-img" style="left:234px;background:linear-gradient(135deg,#a2583a,#c47a52 50%,#7e3f27)" role="img" aria-label="Close-up of cedar shake roofing"></div>
<div class="roof-img" style="left:484px;background:linear-gradient(135deg,#6c6c6c,#9a9a9a 50%,#565656)" role="img" aria-label="Close-up of grey roof shingles"></div>
<div class="roof-img" style="left:733px;background:linear-gradient(135deg,#8a6d62,#b09186 50%,#6f5a52)" role="img" aria-label="Close-up of weathered clay-coloured roof tiles"></div>

<section class="projects" role="img" aria-label="Recent projects band with a faint house photo behind blue">
  <h2 class="section-title">RECENT PROJECTS</h2>
  <div class="tile" style="left:234px;top:108px;width:354px;height:309px;background:linear-gradient(180deg,#3c4650,#5a6068 45%,#2a2e33)" role="img" aria-label="Project photo of a house in Lexington with a company truck in the driveway">
    <div class="tile-label">Lexington</div>
  </div>
  <div class="tile" style="left:594px;top:108px;width:183px;height:150px;background:linear-gradient(180deg,#3f7fd0,#9cc3ea 50%,#3f5238)" role="img" aria-label="Project photo of a colonial house roof"></div>
  <div class="tile" style="left:783px;top:108px;width:183px;height:150px;background:linear-gradient(180deg,#c9d3dc,#a67f6e 55%,#6c5a4e)" role="img" aria-label="Project photo of a brick shingle-style home"></div>
  <div class="tile" style="left:594px;top:266px;width:183px;height:151px;background:linear-gradient(180deg,#7aa35a,#41513a 50%,#2f3c2e)" role="img" aria-label="Project photo of a house framed by trees"></div>
  <div class="tile" style="left:783px;top:266px;width:183px;height:151px;background:linear-gradient(180deg,#b6c7d8,#4d545b 55%,#6d7158)" role="img" aria-label="Project photo of a grey house with three dormers"></div>
</section>

<h2 class="section-title" style="top:2485px">INSTANT ESTIMATE</h2>
<div class="step" style="left:234px"><b>1</b>Choose Your Roof Type</div>
<div class="step" style="left:421px"><b>2</b>About your roof</div>
<div class="step" style="left:608px"><b>3</b>Roof condition</div>
<div class="step" style="left:795px"><b>4</b>Get your cost</div>

<div class="est" style="left:234px">
  <div class="shingle" style="background:linear-gradient(180deg,#58625e,#7a8580 50%,#3e4543)" role="img" aria-label="Grey-green architectural shingle sample"></div>
  <div class="grade">Good</div><div class="model">Summit Ridge HDX</div><div class="price">$$$</div><div class="info">View Info</div>
  <div class="btn-blue">CALCULATE YOUR COST</div>
</div>
<div class="est" style="left:421px">
  <div class="shingle" style="background:linear-gradient(180deg,#7a5a4b,#a17e6c 50%,#5f463b)" role="img" aria-label="Brown blend architectural shingle sample"></div>
  <div class="grade">Good</div><div class="model">Summit Ridge HDX</div><div class="price">$$$</div><div class="info">View Info</div>
  <div class="btn-blue">CALCULATE YOUR COST</div>
</div>
<div class="est" style="left:608px">
  <div class="shingle" style="background:linear-gradient(180deg,#4b5563,#6f7c8c 50%,#323a44)" role="img" aria-label="Slate-blue architectural shingle sample"></div>
  <div class="grade">Good</div><div class="model">Summit Ridge HDX</div><div class="price">$$$</div><div class="info">View Info</div>
  <div class="btn-blue">CALCULATE YOUR COST</div>
</div>
<div class="est" style="left:795px">
  <div class="shingle" style="background:linear-gradient(180deg,#505050,#6e6e6e 50%,#3a3a3a)" role="img" aria-label="Charcoal architectural shingle sample"></div>
  <div class="grade">Good</div><div class="model">Summit Ridge HDX</div><div class="price">$$$</div><div class="info">View Info</div>
  <div class="btn-blue">CALCULATE YOUR COST</div>
</div>

<h2 class="section-title" style="top:3040px">HAPPY CLIENTS</h2>

<div class="quote side" style="left:234px">
  <svg class="mark" width="28" height="16" viewBox="0 0 28 16" fill="#d6d6d6"><circle cx="6" cy="6" r="6"/><path d="M1 8l5 8 3-6z"/><circle cx="20" cy="6" r="6"/><path d="M15 8l5 8 3-6z"/></svg>
  “We needed to put a new roof on our house, as well as repair a sagging porch roof. Shingles had been flying off and we had had several leaks. Evan provided a very reasonable estimate - well below some of the other HomeFinder companies.”
</div>
<div class="quote main" style="left:484px">
  <svg class="mark" width="28" height="16" viewBox="0 0 28 16" fill="#fff"><circle cx="6" cy="6" r="6"/><path d="M1 8l5 8 3-6z"/><circle cx="20" cy="6" r="6"/><path d="M15 8l5 8 3-6z"/></svg>
  “We needed to put a new roof on our house, as well as repair a sagging porch roof. Shingles had been flying off and we had had several leaks. Evan provided a very reasonable estimate - well below some of the other HomeFinder companies.”
</div>
<div class="quote side" style="left:762px">
  <svg class="mark" width="28" height="16" viewBox="0 0 28 16" fill="#d6d6d6"><circle cx="6" cy="6" r="6"/><path d="M1 8l5 8 3-6z"/><circle cx="20" cy="6" r="6"/><path d="M15 8l5 8 3-6z"/></svg>
  “We needed to put a new roof on our house, as well as repair a sagging porch roof. Shingles had been flying off and we had had several leaks. Evan provided a very reasonable estimate - well below some of the other HomeFinder companies.”
</div>
<div class="client" style="left:234px;color:#b5b5b5"><b>Dana</b><span>Brookfield</span></div>
<div class="client" style="left:500px;color:#333"><b>Dana</b><span>Brookfield</span></div>
<div class="client" style="left:762px;color:#b5b5b5"><b>Dana</b><span>Brookfield</span></div>

<footer class="footer">
  <div class="fname"><i></i>RIDGELINE ROOFING</div>
  <div class="addr">48 Elm Row<br>Brookfield MA 01506</div>
  <h4 style="left:548px">QUICK LINKS</h4>
  <div class="links">
    <span>HOME</span><span>ABOUT</span>
    <span>RIDGELINE ROOFING</span><span>SERVICES</span>
    <span>BLOG</span><span>AFFILIATIONS</span>
    <span>REVIEWS</span><span>CONTACT</span>
  </div>
  <h4 style="left:797px">CONTACT</h4>
  <div class="contact">
    <div><svg width="11" height="11" viewBox="0 0 24 24" fill="none" stroke="#999" stroke-width="2"><path d="M5 3h4l2 5-3 2a12 12 0 0 0 6 6l2-3 5 2v4a2 2 0 0 1-2 2A18 18 0 0 1 3 5a2 2 0 0 1 2-2z"/></svg>555-014-2290</div>
    <div><svg width="11" height="11" viewBox="0 0 24 24" fill="none" stroke="#999" stroke-width="2"><path d="M5 3h4l2 5-3 2a12 12 0 0 0 6 6l2-3 5 2v4a2 2 0 0 1-2 2A18 18 0 0 1 3 5a2 2 0 0 1 2-2z"/></svg>555-014-2290</div>
    <div><svg width="12" height="9" viewBox="0 0 26 18" fill="none" stroke="#999" stroke-width="2"><rect x="1" y="1" width="24" height="16"/><path d="M1 1l12 9 12-9"/></svg>hello@ridgelineroofing.example</div>
    <div class="fsocial"><span></span><span></span><span></span><span></span></div>
  </div>
</footer>

</body>
</html>
```